Specialty Plumbing Distributor Advertisement Flyer

We are looking to design a flyer to catch the eye of backflow preventer training schools and instructors and advertise a program we have here. Our company specializes in repair parts, tools, technical assistance etc. and through this no-cost program, we donate educational material to assist trainers for their classes. We offer coupons, store credit and free resources on website. It is called our “Keystone Mentor Initiative” and we also have a page on our website dedicated to the trainers we work with, where we send customers of ours that need backflow schooling.
Plumbing Training Schools
Education

```html
<!DOCTYPE html>
<html lang="en">
<head>
<meta charset="utf-8">
<title>Keystone Mentor Initiative Flyer</title>
<link href="https://fonts.googleapis.com/css2?family=Montserrat:wght@300;400;800;900&family=Oswald:wght@400;600;700&family=Mulish:wght@400;600&display=swap" rel="stylesheet">
<style>
  :root {
    --red: #e8184f;
    --blue: #3c4fa1;
    --white: #ffffff;
    --page-bg: #ece9e4;
    --steel-light: #eeeff0;
    --steel-dark: #d3d5d8;
    --ink-blue: #34479a;
  }
  html, body {
    margin: 0;
    padding: 0;
    width: 986px;
    height: 1200px;
    overflow: hidden;
    background: var(--page-bg);
  }
  .flyer {
    position: absolute;
    left: 79px;
    top: 16px;
    width: 828px;
    height: 1168px;
    box-shadow: 0 4px 18px rgba(0,0,0,0.18);
  }
  .flyer svg { display: block; }
  .headline-big { font-family: 'Montserrat', sans-serif; font-weight: 900; fill: var(--white); }
  .headline-thin { font-family: 'Montserrat', sans-serif; font-weight: 300; fill: var(--white); }
  .band-bold { font-family: 'Montserrat', sans-serif; font-weight: 800; fill: var(--white); }
  .band-sub { font-family: 'Montserrat', sans-serif; font-weight: 400; fill: var(--white); }
  .offer-title { font-family: 'Oswald', sans-serif; font-weight: 600; fill: var(--white); }
  .offer-item { font-family: 'Montserrat', sans-serif; font-weight: 800; fill: var(--white); }
  .offer-item-light { font-family: 'Montserrat', sans-serif; font-weight: 400; fill: var(--white); }
  .donate-title { font-family: 'Oswald', sans-serif; font-weight: 700; fill: var(--red); }
  .donate-sub { font-family: 'Montserrat', sans-serif; font-weight: 400; fill: var(--ink-blue); }
  .donate-classes { font-family: 'Montserrat', sans-serif; font-weight: 400; fill: var(--ink-blue); }
  .products-lead { font-family: 'Montserrat', sans-serif; font-weight: 400; fill: var(--ink-blue); }
  .products-title { font-family: 'Oswald', sans-serif; font-weight: 600; fill: var(--red); }
  .product-item { font-family: 'Mulish', sans-serif; font-weight: 600; fill: #2c2c34; }
  .product-star { fill: var(--blue); }
  .brand-name { font-family: 'Montserrat', sans-serif; font-weight: 400; fill: var(--blue); }
  .contact-text { font-family: 'Mulish', sans-serif; font-weight: 600; fill: var(--white); }
</style>
</head>
<body>
<div class="flyer">
  <svg width="828" height="1168" viewBox="0 0 955 1347" xmlns="http://www.w3.org/2000/svg">
    <defs>
      <linearGradient id="steel" x1="0" y1="0" x2="1" y2="0">
        <stop offset="0" stop-color="var(--steel-dark)"/>
        <stop offset="0.5" stop-color="var(--steel-light)"/>
        <stop offset="1" stop-color="var(--steel-dark)"/>
      </linearGradient>
      <linearGradient id="buildingTones" x1="0" y1="0" x2="0" y2="1">
        <stop offset="0" stop-color="#b9c6d6"/>
        <stop offset="0.35" stop-color="#2a3f86"/>
        <stop offset="0.55" stop-color="#2d4a2c"/>
        <stop offset="1" stop-color="#5f7f3c"/>
      </linearGradient>
      <linearGradient id="classroomTones" x1="0" y1="0" x2="1" y2="1">
        <stop offset="0" stop-color="#e6e7e9"/>
        <stop offset="0.6" stop-color="#9a9ca2"/>
        <stop offset="1" stop-color="#c9cacd"/>
      </linearGradient>
      <linearGradient id="pipeTones" x1="0" y1="0" x2="1" y2="1">
        <stop offset="0" stop-color="#d8d3cc"/>
        <stop offset="0.6" stop-color="#a88a6a"/>
        <stop offset="1" stop-color="#3e62b6"/>
      </linearGradient>
      <linearGradient id="brassTones" x1="0" y1="0" x2="0" y2="1">
        <stop offset="0" stop-color="#d9314a"/>
        <stop offset="0.3" stop-color="#d8b46a"/>
        <stop offset="1" stop-color="#b99450"/>
      </linearGradient>
      <linearGradient id="pumpTones" x1="0" y1="0" x2="1" y2="1">
        <stop offset="0" stop-color="#e2312e"/>
        <stop offset="1" stop-color="#a81616"/>
      </linearGradient>
    </defs>

    <!-- base panels -->
    <rect class="steel-panel" x="0" y="0" width="955" height="1030" fill="url(#steel)"/>
    <rect class="footer-panel" x="0" y="1030" width="955" height="317" fill="var(--white)"/>

    <!-- photo areas -->
    <polygon class="photo-building" role="img" aria-label="Photo of the training hall building with lawn and sign" points="110,0 955,0 955,118 587,478" fill="url(#buildingTones)"/>
    <polygon class="photo-classroom" role="img" aria-label="Photo of students working at backflow test stations" points="0,190 325,515 0,840" fill="url(#classroomTones)"/>
    <polygon class="photo-test-rig" role="img" aria-label="Photo of backflow preventer test rig with piping and valves" points="602,490 955,135 955,490" fill="url(#pipeTones)"/>

    <!-- separators -->
    <line x1="110" y1="0" x2="587" y2="478" stroke="var(--white)" stroke-width="8"/>
    <line x1="587" y1="478" x2="955" y2="118" stroke="var(--white)" stroke-width="8"/>
    <line x1="0" y1="190" x2="325" y2="515" stroke="var(--white)" stroke-width="8"/>

    <!-- red band -->
    <polygon class="band-red" points="0,0 106,0 475,365 325,515 0,190" fill="var(--red)"/>
    <!-- blue band -->
    <polygon class="band-blue" points="0,840 475,365 587,478 0,1060" fill="var(--blue)"/>

    <!-- red band text -->
    <text class="headline-big" x="35" y="42" font-size="92" textLength="540" lengthAdjust="spacingAndGlyphs" transform="rotate(45 35 42)">KEYSTONE</text>
    <text class="headline-thin" x="12" y="94" font-size="44" textLength="505" lengthAdjust="spacingAndGlyphs" transform="rotate(45 12 94)">MENTOR INITIATIVE</text>

    <!-- blue band text -->
    <text class="band-bold" x="19" y="914" font-size="46" textLength="650" lengthAdjust="spacingAndGlyphs" transform="rotate(-45 19 914)">OUR COMPANY SPECIALIZES IN</text>
    <text class="band-sub" x="58" y="950" font-size="25" textLength="640" lengthAdjust="spacingAndGlyphs" transform="rotate(-45 58 950)">REPAIR PARTS, TOOLS, TECHNICAL ASSISTANCE ETC.</text>

    <!-- offer card -->
    <g class="offer-card">
      <rect x="543" y="523" width="379" height="290" rx="16" fill="var(--red)"/>
      <path d="M543,620 V539 a16,16 0 0 1 16,-16 H906 a16,16 0 0 1 16,16 V620 Z" fill="var(--blue)"/>
      <rect x="554" y="534" width="357" height="268" rx="10" fill="none" stroke="var(--white)" stroke-width="2" stroke-dasharray="9 6"/>
      <text class="offer-title" x="732" y="608" font-size="80" text-anchor="middle" textLength="300" lengthAdjust="spacingAndGlyphs">WE OFFER</text>
      <text class="offer-item" x="732" y="666" font-size="36" text-anchor="middle">COUPONS</text>
      <line x1="600" y1="678" x2="865" y2="678" stroke="#f47a98" stroke-width="1.5"/>
      <text class="offer-item" x="732" y="711" font-size="28" text-anchor="middle">STORE CREDIT</text>
      <line x1="600" y1="723" x2="865" y2="723" stroke="#f47a98" stroke-width="1.5"/>
      <text class="offer-item" x="732" y="752" font-size="24" text-anchor="middle">FREE RESOURCES</text>
      <text class="offer-item-light" x="732" y="784" font-size="33" text-anchor="middle">ON WEBSITE</text>
    </g>

    <!-- product illustrations -->
    <rect class="valve-illustration" role="img" aria-label="Illustration of a brass pressure relief valve" x="232" y="813" width="72" height="187" rx="8" fill="url(#brassTones)"/>

    <!-- donate block -->
    <text class="donate-title" x="922" y="932" font-size="112" text-anchor="end" textLength="484" lengthAdjust="spacingAndGlyphs">WE DONATE</text>
    <text class="donate-sub" x="922" y="960" font-size="21" text-anchor="end" textLength="488" lengthAdjust="spacingAndGlyphs">EDUCATIONAL MATERIAL TO ASSIST TRAINERS</text>
    <text class="donate-classes" x="922" y="1010" font-size="52" text-anchor="end" textLength="490" lengthAdjust="spacingAndGlyphs">FOR THEIR CLASSES</text>

    <rect class="pump-illustration" role="img" aria-label="Illustration of a red fire pump assembly on a base" x="60" y="1035" width="300" height="200" rx="10" fill="url(#pumpTones)"/>

    <!-- product types -->
    <text class="products-lead" x="900" y="1074" font-size="27" text-anchor="end" textLength="292" lengthAdjust="spacingAndGlyphs">THE PRODUCT TYPES</text>
    <text class="products-title" x="908" y="1126" font-size="48" text-anchor="end" textLength="486" lengthAdjust="spacingAndGlyphs">WE WILL BE CARRYING ARE</text>

    <g class="product-list">
      <text class="product-star" x="506" y="1170" font-size="16">★</text>
      <text class="product-item" x="537" y="1170" font-size="18">Fire Pump repack kits</text>
      <text class="product-star" x="506" y="1203" font-size="16">★</text>
      <text class="product-item" x="537" y="1203" font-size="18">Fast Packs</text>
      <text class="product-star" x="506" y="1236" font-size="16">★</text>
      <text class="product-item" x="537" y="1236" font-size="18">Gland Bolt Assemblies</text>
      <text class="product-star" x="506" y="1269" font-size="16">★</text>
      <text class="product-item" x="537" y="1269" font-size="18">Lantern Rings</text>

      <text class="product-star" x="759" y="1167" font-size="16">★</text>
      <text class="product-item" x="788" y="1167" font-size="18">Case Gaskets</text>
      <text class="product-star" x="759" y="1200" font-size="16">★</text>
      <text class="product-item" x="788" y="1200" font-size="18">Packing</text>
      <text class="product-star" x="759" y="1233" font-size="16">★</text>
      <text class="product-item" x="788" y="1233" font-size="18">Bearings</text>
      <text class="product-star" x="759" y="1266" font-size="16">★</text>
      <text class="product-item" x="788" y="1266" font-size="18">Jockey Pumps</text>
    </g>

    <!-- brand -->
    <rect class="brand-square" x="52" y="1282" width="30" height="30" fill="var(--blue)"/>
    <text class="brand-name" x="96" y="1308" font-size="29">Summit Valve Supply Co.</text>

    <!-- contact bar -->
    <polygon class="contact-bar" points="460,1347 510,1295 955,1295 955,1347" fill="var(--blue)"/>
    <g class="icon-web" fill="none" stroke="var(--white)" stroke-width="1.6">
      <circle cx="533" cy="1322" r="12"/>
      <ellipse cx="533" cy="1322" rx="5" ry="12"/>
      <line x1="521" y1="1322" x2="545" y2="1322"/>
    </g>
    <text class="contact-text" x="554" y="1329" font-size="18">www.valvepartshub.com</text>
    <line x1="758" y1="1305" x2="758" y2="1339" stroke="var(--white)" stroke-width="2"/>
    <g class="icon-phone">
      <circle cx="781" cy="1322" r="12" fill="none" stroke="var(--white)" stroke-width="1.6"/>
      <path d="M776,1315 q-2,2 0,6 q3,6 8,8 q3,1 5,-1 l-3,-3 q-1,1 -3,0 q-3,-2 -4,-5 q0,-1 1,-2 z" fill="var(--white)"/>
    </g>
    <text class="contact-text" x="800" y="1329" font-size="18">800.555.0142</text>
  </svg>
</div>
</body>
</html>
```